Billboard design - consider what a billboard is

Design a billboard using my logo - Billboard is 6m x 3m
A Billboard is advertising for my company that is on a big sign.

Has to be clean and easy to read, and ideally highlights that we are Residential and Commercial builders.

Keep it clean and easy to read

The contact number for the board is

022 583 7092
www.harbourframeworks.co.nz
info@harbourframeworks.co.nz

Doesnt have to have all contact details if it doesnt fit

Has to catch peoples attention to contact us if they need a builder

Can you please change the sign to be all white writing, with black background ?
Updates

Please consider what a billboard is...

The design needs to be suitable for a billboard..

Target Market(s)

people driving past

Industry/Entity Type

Construction

Logo Text

Wellington Builder, website email address, contact number

Colors
0054AA
0677BA
7BADD7
CADEEF
E8F1F8

Requirements
Must have
• Easy to read
Nice to have
• easy to read, can clearly see contact details

```html
<!DOCTYPE html>
<html lang="en">
<head>
<meta charset="utf-8">
<title>Harbour Frameworks Billboard</title>
<link rel="stylesheet" href="https://fonts.googleapis.com/css2?family=Poppins:wght@500;700&display=swap">
<style>
  :root {
    --stage: #9a9a9a;
    --paper: #ffffff;
    --slate: #66665f;
    --sky: #5b8ac9;
    --mark: #6b5f5f;
  }
  * { margin: 0; padding: 0; box-sizing: border-box; }
  html, body {
    width: 867px; height: 1200px; overflow: hidden;
    background: var(--stage);
    font-family: "Poppins", Arial, sans-serif;
  }
  .billboard {
    position: absolute; left: 75px; top: 729px;
    width: 717px; height: 358px;
    background: var(--paper);
    box-shadow: 0 6px 18px rgba(0,0,0,0.25);
    overflow: hidden;
  }
  .headline-panel { position: relative; height: 212px; }
  .divider { position: absolute; left: 0; top: 0; width: 717px; height: 212px; }
  .headline {
    position: absolute; left: 20px; top: 18px;
    font-weight: 700; line-height: 0.96; color: var(--slate);
    letter-spacing: -1px;
  }
  .headline .line { display: block; font-size: 53px; }
  .headline .builders { font-size: 76px; color: var(--sky); margin-top: 2px; letter-spacing: -2px; }
  .brand {
    position: absolute; left: 478px; top: 66px;
    display: flex; align-items: center; gap: 10px;
  }
  .brand-square { width: 18px; height: 90px; background: var(--mark); }
  .brand-name {
    font-weight: 700; font-size: 28px; line-height: 1.1; color: var(--sky);
    letter-spacing: -0.3px; white-space: nowrap;
  }
  .call-band {
    height: 70px; background: var(--slate); color: var(--paper);
    display: flex; align-items: center; padding-left: 21px;
    font-weight: 700; font-size: 46px; letter-spacing: -1.2px; white-space: nowrap;
  }
  .call-band .phone { margin-left: 22px; }
  .web-band {
    height: 76px; background: var(--sky); color: var(--paper);
    display: flex; align-items: center; padding-left: 23px;
    font-weight: 500; font-size: 44px; letter-spacing: -0.5px; white-space: nowrap;
  }
</style>
</head>
<body>
  <main class="billboard">
    <section class="headline-panel">
      <svg class="divider" viewBox="0 0 717 212" aria-hidden="true">
        <polygon points="471,0 483,0 391,212 379,212" fill="var(--sky)"/>
        <polygon points="483,0 497,0 405,212 391,212" fill="var(--slate)"/>
      </svg>
      <h1 class="headline">
        <span class="line">RESIDENTIAL &amp;</span>
        <span class="line">COMMERCIAL</span>
        <span class="line builders">BUILDERS</span>
      </h1>
      <div class="brand">
        <span class="brand-square" aria-hidden="true"></span>
        <span class="brand-name">Harbour<br>Frameworks</span>
      </div>
    </section>
    <section class="call-band">
      <span class="call-label">CALL US TODAY!</span>
      <span class="phone">022 583 7092</span>
    </section>
    <section class="web-band">www.harbourframeworks.co.nz</section>
  </main>
</body>
</html>
```